Womans Supplement Designs

Launching a Supplement company and need to get some initial designs created, I've attached our logo and the bottle type that I want the samples done one.

This project is for our Whey Protein we are starting with Vanilla, chocolate and strawberry banana

(ALL DESIGN VARIATIONS MUST BE A WHITE BOTTLE NOT BLACK)

(FOR DESIGN SAMPLES PLEASE USE THE SUPPLEMENT BOTTLE STYLE I PROVIDED)

Whoever is selected the winner I will have more work for you to complete the disigns for the rest of the products in the line, Just want to get this shake completed first

Target Market(s)

Women

Requirements
Must have
• Must have our current logo involved

the name of this product will be "KIVA LUM"

Must have this slogan,

ALL-IN-ONE PREMIUM PROTEIN NUTRITIONAL SHAKE FOR BLACK WOMEN

This is our meal replacement

the design should try to keep the same look and feel of the existing provided supplement images

we are starting with chocolate, vanilla and strawberry banana

this is for women and should look colorful and appeal to them
Should not have
• Do not use an image of a person or lady, don't want it branded to a person

```html
<!DOCTYPE html>
<html lang="en">
<head>
<meta charset="utf-8">
<title>KIVA LUM – All-in-One Protein Shake Label</title>
<link rel="stylesheet" href="https://fonts.googleapis.com/css2?family=Michroma&family=Orbitron:wght@500;700;800&display=swap">
<style>
  :root {
    --magenta: #bc2a5e;
    --ink: #000000;
    --paper: #ffffff;
    --hex-tint: #f3c9d7;
  }
  html, body {
    margin: 0;
    padding: 0;
    width: 805px;
    height: 1200px;
    overflow: hidden;
    background: var(--paper);
  }
  .canvas {
    position: relative;
    width: 805px;
    height: 1200px;
    background: var(--paper);
  }
  .label {
    position: absolute;
    left: 0;
    top: 259px;
    width: 805px;
    height: 682px;
    display: block;
  }
  .band { fill: var(--magenta); }
  .tag-box { fill: var(--paper); }
  .claim-all {
    font-family: "Michroma", sans-serif;
    font-size: 48px;
    fill: var(--ink);
  }
  .product-name {
    font-family: "Orbitron", sans-serif;
    font-weight: 800;
    font-size: 124px;
    fill: var(--ink);
  }
  .slogan {
    font-family: "Michroma", sans-serif;
    font-size: 32px;
    fill: var(--ink);
  }
  .brand-name {
    font-family: "Michroma", sans-serif;
    font-size: 22px;
    fill: var(--ink);
  }
  .flavour {
    font-family: "Orbitron", sans-serif;
    font-weight: 700;
    font-size: 24px;
    fill: var(--ink);
  }
  .stat-value {
    font-family: "Orbitron", sans-serif;
    font-weight: 700;
    font-size: 18px;
    fill: var(--paper);
  }
  .stat-label {
    font-family: "Michroma", sans-serif;
    font-size: 8px;
    fill: var(--paper);
  }
  .stat-sub {
    font-family: "Michroma", sans-serif;
    font-size: 5px;
    fill: var(--paper);
  }
  .net-weight {
    font-family: "Orbitron", sans-serif;
    font-weight: 500;
    font-size: 17px;
    fill: var(--ink);
  }
  .servings-count {
    font-family: "Orbitron", sans-serif;
    font-weight: 700;
    font-size: 44px;
    fill: var(--ink);
  }
  .servings-word {
    font-family: "Michroma", sans-serif;
    font-size: 14px;
    fill: var(--ink);
  }
</style>
</head>
<body>
<main class="canvas">
  <svg class="label" viewBox="0 0 1416 1200" xmlns="http://www.w3.org/2000/svg">
    <defs>
      <radialGradient id="hexGlow" cx="50%" cy="50%" r="50%">
        <stop offset="0%" stop-color="#f3c9d7" stop-opacity="0.55"/>
        <stop offset="100%" stop-color="#f3c9d7" stop-opacity="0"/>
      </radialGradient>
    </defs>

    <g class="hex-texture" role="img" aria-label="Faint pink honeycomb pattern">
      <ellipse cx="300" cy="230" rx="190" ry="150" fill="url(#hexGlow)"/>
      <ellipse cx="560" cy="880" rx="210" ry="170" fill="url(#hexGlow)"/>
      <ellipse cx="780" cy="540" rx="170" ry="130" fill="url(#hexGlow)"/>
    </g>

    <!-- left spine -->
    <rect class="band" x="167" y="0" width="81" height="1130"/>
    <rect class="tag-box" x="150" y="190" width="43" height="435"/>
    <text class="claim-all" transform="translate(188 620) rotate(-90)" textLength="420" lengthAdjust="spacingAndGlyphs">ALL-IN-ONE</text>

    <!-- product name and slogan -->
    <text class="product-name" transform="translate(390 1090) rotate(-90)" textLength="792" lengthAdjust="spacingAndGlyphs">KIVA LUM</text>
    <text class="slogan" transform="translate(464 1085) rotate(-90)" textLength="788" lengthAdjust="spacingAndGlyphs">PREMIUM PROTEIN NUTRITIONAL</text>
    <text class="slogan" transform="translate(508 1085) rotate(-90)" textLength="662" lengthAdjust="spacingAndGlyphs">SHAKE FOR BLACK WOMEN</text>

    <!-- brand -->
    <g class="brand">
      <rect x="418" y="110" width="22" height="22" fill="var(--ink)"/>
      <text class="brand-name" x="430" y="172" text-anchor="middle">NERA VITA</text>
    </g>

    <!-- diagonal stripes -->
    <polygon class="band" points="700,0 790,0 1416,939 1416,1074"/>
    <polygon class="band" points="900,0 945,0 1416,706 1416,774"/>
    <polygon class="band" points="1060,0 1416,0 1416,534"/>
    <polygon class="band" points="787,732 852,732 1112,1130 1047,1130"/>

    <!-- flavour and nutrition tags -->
    <text class="flavour" x="780" y="718" textLength="205" lengthAdjust="spacingAndGlyphs">CHOCOLATE</text>

    <g class="stat">
      <polygon class="band" points="885,733 985,733 1040,815 940,815"/>
      <text class="stat-value" x="965" y="771" text-anchor="middle">20g</text>
      <text class="stat-label" x="962" y="786" text-anchor="middle">PROTEIN</text>
      <text class="stat-sub" x="962" y="793" text-anchor="middle">PER SCOOP</text>
    </g>
    <g class="stat">
      <polygon class="band" points="950,833 1050,833 1105,913 1005,913"/>
      <text class="stat-value" x="1031" y="868" text-anchor="middle">1g</text>
      <text class="stat-label" x="1029" y="882" text-anchor="middle">SUGAR</text>
      <text class="stat-sub" x="1029" y="889" text-anchor="middle">PER SCOOP</text>
    </g>
    <g class="stat">
      <polygon class="band" points="1013,931 1113,931 1168,1013 1068,1013"/>
      <text class="stat-value" x="1093" y="968" text-anchor="middle">4g</text>
      <text class="stat-label" x="1091" y="983" text-anchor="middle">FIBER</text>
      <text class="stat-sub" x="1091" y="990" text-anchor="middle">PER SCOOP</text>
    </g>

    <!-- quantity -->
    <text class="net-weight" x="608" y="1100" textLength="172" lengthAdjust="spacingAndGlyphs">1,050G(2.3LBS)</text>
    <text class="servings-count" x="898" y="1087" textLength="82" lengthAdjust="spacingAndGlyphs">30</text>
    <text class="servings-word" x="898" y="1110" textLength="86" lengthAdjust="spacingAndGlyphs">servings</text>
  </svg>
</main>
</body>
</html>
```